Flyer Design Project

Need a DL Size flyer (2 sided) for letter box marketing for our website www.brightwardsecure.com.au

Project Deadline Extended
Reason: Thank you for submitting the designs. We like few of the designs and will request those designers to changes few things to make it more suitable for us. Because of holidays need to extend the deadlines. Thank you.

Industry/Entity Type

Marketing

```html
<!DOCTYPE html>
<html lang="en">
<head>
<meta charset="utf-8">
<title>Brightward Secure DL Flyer</title>
<link href="https://fonts.googleapis.com/css2?family=Titillium+Web:wght@400;600;700&display=swap" rel="stylesheet">
<style>
:root{
  --bg:#d9d9d9;
  --paper:#ffffff;
  --tint:#c3d6e8;
  --blue:#2f6fb3;
  --title:#7fa7d3;
  --navy:#1d3f73;
  --ink:#4a4f57;
  --muted:#8a9aab;
  --rule:#2a5ea8;
  --photo:#9aa3ad;
}
*{box-sizing:border-box;margin:0;padding:0}
html,body{width:1200px;height:861px;overflow:hidden;background:var(--bg);font-family:"Titillium Web",sans-serif;color:var(--ink)}
.stage{position:relative;width:1200px;height:861px}
.flyer{position:absolute;top:110px;width:310px;height:640px;background:var(--paper);box-shadow:0 6px 18px rgba(0,0,0,.25);overflow:hidden}
.flyer--front{left:265px;background:linear-gradient(180deg,#fff 0%,#fff 35%,var(--tint) 100%)}
.flyer--back{left:625px;background:linear-gradient(180deg,#e2ecf5 0%,#fff 22%,#fff 100%)}
.top-band{height:26px;background:linear-gradient(180deg,#f2f5f9 0,#c7d3e2 45%,#5d7fa8 70%,#9fb4cc 100%)}
.brand-title{font-size:34px;font-weight:700;color:var(--title);text-align:center;margin:8px 0 4px;letter-spacing:.5px}
.section-head{font-size:13px;font-weight:700;color:var(--blue);margin:0 0 3px}
.section-head span{font-weight:400}
.body-text{font-size:9.5px;line-height:1.25;color:var(--ink)}
.front-inner{padding:0 18px}
.about{display:flex;gap:6px}
.about .body-text{width:150px}
.photo{background:radial-gradient(circle at 45% 40%,#f4f4f4,var(--photo));border-radius:4px}
.camera{width:90px;height:90px;border-radius:50%;margin-top:6px}
.solutions{margin:8px 0 10px}
.partners{display:grid;grid-template-columns:repeat(3,1fr);row-gap:10px;margin:4px 0 14px;text-align:center}
.partner{font-size:14px;font-weight:700;color:var(--navy)}
.list{list-style:none;font-size:9.5px;line-height:1.25}
.list li{padding-left:10px;position:relative}
.list li::before{content:"";position:absolute;left:1px;top:5px;width:4px;height:4px;border-radius:50%;background:var(--ink)}
.row{display:flex;justify-content:space-between;align-items:flex-start;margin-bottom:10px}
.phones{width:68px;height:62px;margin-top:38px}
.monitor{width:72px;height:50px;margin-top:8px}
.contact dl{display:grid;grid-template-columns:38px 1fr;font-size:9px;line-height:1.25}
.contact dt{font-weight:700;color:var(--navy)}
.back-inner{padding:28px 16px 0}
.intro{font-size:9px;line-height:1.25;color:var(--muted);margin:6px 0 10px}
.package{position:relative;height:74px;display:flex;justify-content:space-between;padding:4px 4px 0;border-bottom:1px solid var(--rule)}
.package::after{content:"";position:absolute;right:-4px;bottom:-3px;width:5px;height:5px;border-radius:50%;background:var(--rule)}
.pkg-text{width:140px}
.pkg-name{font-size:10.5px;font-weight:700;color:var(--navy);line-height:1}
.pkg-sub{font-size:7.5px;font-weight:700;color:var(--ink);line-height:1.2}
.pkg-desc{font-size:7px;line-height:1.2;color:var(--ink)}
.pkg-side{width:118px;display:flex;flex-direction:column;align-items:center}
.kit{width:112px;height:44px}
.price{font-size:11px;font-weight:700;color:var(--navy);margin-top:2px}
.price small{font-size:7px;font-weight:400;color:var(--ink)}
.foot-band{position:absolute;left:0;right:0;bottom:0;height:34px;background:linear-gradient(180deg,#fff 0,#9fb4cc 30%,#1d3f73 55%,#5d7fa8 75%,#dfe7f0 100%)}
</style>
</head>
<body>
<main class="stage">

  <section class="flyer flyer--front">
    <div class="top-band"></div>
    <div class="front-inner">
      <h1 class="brand-title">Brightward Secure</h1>
      <div class="about">
        <div>
          <h2 class="section-head">About <span>Us</span></h2>
          <p class="body-text">We are a Sydney based company, providing high quality and affordable CCTV security system for home &amp; business clients since 2009. We have extensive experience and knowledge in the design, installation, maintenance and repair of wide range of CCTV systems.</p>
        </div>
        <div class="photo camera" role="img" aria-label="Photo of a white dome security camera"></div>
      </div>
      <p class="body-text solutions">We can provide a wide range of home and business solutions – from a single camera system, to complex matrix video surveillance systems with multiple cameras, in multiple locations with 24X7 recording and monitoring.</p>
      <div class="partners">
        <span class="partner">Arvent</span><span class="partner">Norlex</span><span class="partner">Keldon</span>
        <span class="partner">Optiva</span><span class="partner">Sentrel</span><span class="partner">Halcor</span>
      </div>
      <div class="row">
        <div>
          <h2 class="section-head">Our Services <span>Include</span></h2>
          <ul class="list">
            <li>Installing Standalone DVR Sytem</li>
            <li>Installing PC based high quality DVR system</li>
            <li>Installing IP based megapixel CCTV System</li>
            <li>Services for home, office and business clients</li>
            <li>Complete CCTV package from 1 camera to multi sites system</li>
          </ul>
        </div>
        <div class="photo phones" role="img" aria-label="Photo of smartphones showing live camera views"></div>
      </div>
      <div class="row">
        <div>
          <h2 class="section-head">Brightward Secure <span>Guarantee</span></h2>
          <ul class="list">
            <li>High quality hardware</li>
            <li>100% customer satisfaction</li>
            <li>1 year full warranty</li>
            <li>14 days money back guarantee</li>
          </ul>
        </div>
        <div class="photo monitor" role="img" aria-label="Photo of a monitor showing a multi-camera view"></div>
      </div>
      <div class="contact">
        <h2 class="section-head">Contact <span>Us</span></h2>
        <dl>
          <dt>Office</dt><dd>: 14/6 Harlow Street, Kemsley, NSW 2291</dd>
          <dt>Website</dt><dd>: www.brightwardsecure.com.au</dd>
          <dt>Phone</dt><dd>: 02 5550 1834</dd>
        </dl>
      </div>
    </div>
  </section>

  <section class="flyer flyer--back">
    <div class="back-inner">
      <h2 class="section-head">Packages</h2>
      <p class="intro">We offer a variety of CCTV system packages that are reliable, affordable and easy to use. Below are some of the packages that are suitable for a home or small business. If you need a system with more than 4 cameras or have a special need please contact us for a free quote and we will ensure you will be happy and satisfied with our product, service and prices.</p>

      <article class="package">
        <div class="pkg-text"><h3 class="pkg-name">Package 1</h3><p class="pkg-sub">Standalone DVR System (2 Cameras)</p><p class="pkg-desc">2 X high resolution dome cameras, 1 X 4 channel standalone DVR, 500GB hard drive, 19 inches LCD monitor, Remote access from PCs &amp; Phones*, Easy to use, 1 Year Warranty, Full system supplied &amp; installed</p></div>
        <div class="pkg-side"><div class="photo kit" role="img" aria-label="Photo of monitor, DVR and two dome cameras"></div><p class="price">$1495 <small>+ GST*</small></p></div>
      </article>
      <article class="package">
        <div class="pkg-text"><h3 class="pkg-name">Package 2</h3><p class="pkg-sub">Standalone DVR System (4 Cameras)</p><p class="pkg-desc">4 X high resolution dome cameras, 1 X 4 channel standalone DVR, 500GB hard drive, 19 inches LCD monitor, Remote access from PCs &amp; Phones*, Easy to use, 1 Year Warranty, Full system supplied &amp; installed</p></div>
        <div class="pkg-side"><div class="photo kit" role="img" aria-label="Photo of monitor, DVR and four dome cameras"></div><p class="price">$2195 <small>+ GST*</small></p></div>
      </article>
      <article class="package">
        <div class="pkg-text"><h3 class="pkg-name">Package 3</h3><p class="pkg-sub">Standalone DVR System (8 Cameras)</p><p class="pkg-desc">8 X high resolution dome cameras, 1 X 8 channel standalone DVR, 1 Terrabyte hard drive, 19 inches LCD monitor, Remote access from PCs &amp; Phones*, Easy to use, 1 Year Warranty, Full system supplied &amp; installed</p></div>
        <div class="pkg-side"><div class="photo kit" role="img" aria-label="Photo of monitor, DVR and eight dome cameras"></div><p class="price">$3295 <small>+ GST*</small></p></div>
      </article>
      <article class="package">
        <div class="pkg-text"><h3 class="pkg-name">Package 4</h3><p class="pkg-sub">IP based CCTV System (2 Cameras)</p><p class="pkg-desc">2 X 2 Megapixel IP Cameras, 1 X PC based NVR System, 500GB hard drive, 19 inches LCD Monitor, Remote Access from PCs and Phones*, Easy to use, 1 Year warranty, Full system supplied &amp; installed</p></div>
        <div class="pkg-side"><div class="photo kit" role="img" aria-label="Photo of PC, monitor and two IP cameras"></div><p class="price">$1995 <small>+ GST*</small></p></div>
      </article>
      <article class="package">
        <div class="pkg-text"><h3 class="pkg-name">Package 5</h3><p class="pkg-sub">IP based CCTV System (4 Cameras)</p><p class="pkg-desc">4 X 2 Megapixel IP Cameras, 1 X PC based NVR System, 1 Terrabyte hard drive, 19 inches LCD Monitor, Remote Access from PCs and Phones*, Easy to use, 1 Year warranty, Full system supplied &amp; Installed</p></div>
        <div class="pkg-side"><div class="photo kit" role="img" aria-label="Photo of PC, monitor and four IP cameras"></div><p class="price">$3295 <small>+ GST*</small></p></div>
      </article>
      <article class="package">
        <div class="pkg-text"><h3 class="pkg-name">Package 6</h3><p class="pkg-sub">IP based CCTV System (8 Cameras)</p><p class="pkg-desc">8 X 2 Megapixel IP Cameras, 1 X PC based NVR System, 2 Terrabyte hard drive, 19 inches LCD Monitor, Remote Access from PCs and Phones*, Easy to use, 1 Year warranty, Full system supplied &amp; Installed</p></div>
        <div class="pkg-side"><div class="photo kit" role="img" aria-label="Photo of PC, monitor and eight IP cameras"></div><p class="price">$4495 <small>+ GST*</small></p></div>
      </article>
    </div>
    <div class="foot-band"></div>
  </section>

</main>
</body>
</html>
```